Need Business Card for our Indian Grocery Store

Industry/Entity Type

Grocery Store

Contact Information for Business Card

Manoj Varkey
Director

Store Locations:

Kellbridge
482 Fenwick Road
P: 03 9581 2046

Ashvale
613 Larchmont
P: 03 9572 8814

email: pvtstores@mailbrook.net

Requirements
Must have
• Our logo Colours

```html
<!DOCTYPE html>
<html lang="en">
<head>
<meta charset="utf-8">
<title>PVT Stores – Business Card</title>
<link href="https://fonts.googleapis.com/css2?family=Roboto:wght@400;500;700&family=Libre+Baskerville:ital@1&display=swap" rel="stylesheet">
<style>
  :root {
    --page-bg: #ecebe8;
    --card-frost: #e9eaea;
    --brand-red: #d0141b;
    --brand-red-deep: #a80e14;
    --text-light: #ffffff;
    --text-soft: #f6d9da;
  }
  html, body {
    margin: 0;
    width: 1200px;
    height: 969px;
    overflow: hidden;
    background: var(--page-bg);
  }
  .canvas {
    width: 1200px;
    height: 969px;
    display: flex;
    align-items: center;
    justify-content: center;
  }
  .business-card {
    position: relative;
    width: 1000px;
    height: 550px;
    background: var(--card-frost);
    display: flex;
    box-shadow: 0 6px 24px rgba(0,0,0,0.15);
    font-family: "Roboto", Arial, sans-serif;
  }
  .contact-panel {
    width: 390px;
    background: linear-gradient(160deg, var(--brand-red) 0%, var(--brand-red-deep) 100%);
    color: var(--text-light);
    padding: 104px 0 0 44px;
    box-sizing: border-box;
  }
  .person-name {
    font-size: 31px;
    font-weight: 500;
    letter-spacing: 0.5px;
    margin: 0;
    text-transform: uppercase;
  }
  .person-role {
    font-size: 22px;
    font-weight: 500;
    letter-spacing: 1px;
    margin: 2px 0 38px;
    color: var(--text-soft);
  }
  .store {
    font-size: 23px;
    line-height: 32px;
    margin-bottom: 18px;
  }
  .store-suburb { color: var(--text-soft); }
  .store-phone b { font-weight: 700; margin-right: 6px; }
  .online { margin-top: 4px; }
  .online-row {
    display: flex;
    align-items: center;
    gap: 12px;
    font-size: 23px;
    line-height: 34px;
  }
  .online-row svg { width: 20px; height: 20px; flex: none; }
  .brand-side {
    flex: 1;
    position: relative;
    display: flex;
    flex-direction: column;
    align-items: center;
    justify-content: center;
  }
  .brand-frame {
    position: absolute;
    top: 14px;
    right: 14px;
    bottom: 14px;
    left: 0;
    border: 3px solid var(--brand-red);
    border-left: none;
  }
  .brand-name {
    font-family: "Roboto", Arial, sans-serif;
    font-size: 76px;
    font-weight: 700;
    color: var(--brand-red);
    letter-spacing: 4px;
    margin: 0;
  }
  .brand-tagline {
    display: flex;
    align-items: center;
    gap: 14px;
    margin-top: 18px;
    font-family: "Libre Baskerville", Georgia, serif;
    font-style: italic;
    font-size: 22px;
    color: var(--brand-red-deep);
  }
  .brand-tagline::before,
  .brand-tagline::after {
    content: "";
    width: 36px;
    height: 2px;
    background: var(--brand-red-deep);
  }
</style>
</head>
<body>
<main class="canvas">
  <article class="business-card">
    <section class="contact-panel">
      <h1 class="person-name">Manoj Varkey</h1>
      <p class="person-role">DIRECTOR</p>

      <div class="store">
        <div class="store-suburb">Kellbridge</div>
        <div>482 Fenwick Road</div>
        <div class="store-phone"><b>P</b>03 9581 2046</div>
      </div>

      <div class="store">
        <div class="store-suburb">Ashvale</div>
        <div>613 Larchmont</div>
        <div class="store-phone"><b>P</b>03 9572 8814</div>
      </div>

      <div class="online">
        <div class="online-row">
          <svg viewBox="0 0 20 20" aria-hidden="true"><rect x="1" y="4" width="18" height="12" fill="#fff"/><path d="M1 4 L10 11 L19 4" fill="none" stroke="#c0121a" stroke-width="1.6"/></svg>
          <span>pvtstores@mailbrook.net</span>
        </div>
        <div class="online-row">
          <svg viewBox="0 0 20 20" aria-hidden="true"><circle cx="10" cy="10" r="8.5" fill="none" stroke="#fff" stroke-width="1.8"/><ellipse cx="10" cy="10" rx="3.6" ry="8.5" fill="none" stroke="#fff" stroke-width="1.4"/><path d="M1.5 10 H18.5" stroke="#fff" stroke-width="1.4"/></svg>
          <span>www.pvtstores.net</span>
        </div>
      </div>
    </section>

    <section class="brand-side">
      <div class="brand-frame"></div>
      <p class="brand-name">PVT STORES</p>
      <p class="brand-tagline">Fresh Pantry Since 2013</p>
    </section>
  </article>
</main>
</body>
</html>
```